Business Card and Word .doc header and footer required

I need a business card designed for my cybersecurity consulting company. Also required, is a header and footer to be ued for my word documents.
Attached is the Logo design, font and rgb used.

Industry/Entity Type

Cyber Security Consulting

Contact Information for Business Card

Name, Phone, email, website

Colors
0054AA
0677BA
7BADD7
CADEEF
E8F1F8

Requirements
Must have
• Sleek, modern

```html
<!DOCTYPE html>
<html lang="en">
<head>
<meta charset="utf-8">
<title>Harrow Point Consulting – Stationery</title>
<link rel="stylesheet" href="https://fonts.googleapis.com/css2?family=Montserrat:wght@400;500;600;700&family=Open+Sans:wght@400;600&display=swap">
<style>
:root{
  --navy:#131b31;
  --navy-deep:#0d1426;
  --blue-strong:#0054AA;
  --blue:#0677BA;
  --blue-soft:#7BADD7;
  --blue-pale:#CADEEF;
  --blue-mist:#E8F1F8;
  --ink:#1f2430;
  --ink-muted:#5a6170;
  --paper:#ffffff;
  --stage:#dfe4ec;
}
*{box-sizing:border-box;margin:0;padding:0}
html,body{width:769px;height:1200px;overflow:hidden}
body{background:var(--stage);font-family:"Open Sans",Arial,sans-serif;color:var(--ink);position:relative}

.card{position:absolute;top:40px;width:335px;height:192px;overflow:hidden;box-shadow:0 2px 6px rgba(0,0,0,.12)}
.card--front{left:40px;background:linear-gradient(135deg,var(--navy) 0%,var(--navy-deep) 100%);display:flex;flex-direction:column;align-items:center;justify-content:center;gap:12px}
.card--back{left:394px;background:var(--paper)}

.brand-mark{width:46px;height:46px;border-radius:50%;border:4px solid var(--blue)}
.brand-name{font-family:"Montserrat",Arial,sans-serif;font-weight:600;text-align:center;line-height:1.15;letter-spacing:.5px}
.card--front .brand-name{color:var(--paper);font-size:19px}
.brand-name small{display:block;font-size:.42em;letter-spacing:3px}

.card--back .brand{position:absolute;top:16px;right:18px;display:flex;flex-direction:column;align-items:center;gap:5px}
.card--back .brand-mark{width:20px;height:20px;border-width:2px}
.card--back .brand-name{color:var(--blue-strong);font-size:10px}
.watermark-ring{position:absolute;right:-40px;bottom:-70px;width:190px;height:190px;border-radius:50%;border:14px solid var(--blue-mist)}

.person{position:absolute;left:16px;top:62px;border-left:2px solid var(--ink);padding-left:6px}
.person__name{font-family:"Montserrat",Arial,sans-serif;font-weight:600;font-size:14px;color:var(--blue);letter-spacing:.5px}
.person__role{font-family:"Montserrat",Arial,sans-serif;font-size:7.5px;letter-spacing:.5px;color:var(--ink)}

.contact-list{position:absolute;left:16px;top:128px;list-style:none;display:flex;flex-direction:column;gap:5px;font-size:8px;color:var(--ink)}
.contact-list li{display:flex;align-items:center;gap:6px}
.contact-icon{width:9px;height:9px;flex:none}

.letterhead{position:absolute;left:85px;top:300px;width:600px;height:848px;background:var(--paper);box-shadow:0 3px 10px rgba(0,0,0,.12);font-size:10px;line-height:1.6}
.letterhead__band{position:absolute;top:0;right:0;width:210px;height:120px;background:linear-gradient(135deg,var(--navy) 0%,var(--navy-deep) 100%);display:flex;flex-direction:column;align-items:center;justify-content:center;gap:9px}
.letterhead__band .brand-mark{width:30px;height:30px;border-width:3px}
.letterhead__band .brand-name{color:var(--paper);font-size:13px}
.letterhead__body{position:absolute;left:56px;top:70px;width:320px}
.letterhead__to{color:var(--ink-muted);margin-bottom:14px}
.recipient{margin-bottom:18px}
.recipient strong{font-weight:600}
.letter-date{margin-bottom:18px;color:var(--ink-muted)}
.letterhead__text{position:absolute;left:56px;top:290px;width:488px}
.letterhead__text p{margin-bottom:14px}
.signoff{margin-top:30px}
.signoff__name{font-family:"Montserrat",Arial,sans-serif;font-weight:600;color:var(--blue);margin-top:36px}
.letterhead__footer{position:absolute;left:0;right:0;bottom:0;height:54px;border-top:3px solid var(--blue);display:flex;align-items:center;justify-content:center;gap:34px;font-size:9px}
.letterhead__footer span{display:flex;align-items:center;gap:6px}
</style>
</head>
<body>
<svg width="0" height="0" style="position:absolute" aria-hidden="true">
  <defs>
    <symbol id="icon-phone" viewBox="0 0 10 10"><circle cx="5" cy="5" r="5" fill="#0677BA"/><path d="M3.2 2.6l1 .1.4 1.2-.6.5a3.5 3.5 0 0 0 1.6 1.6l.5-.6 1.2.4.1 1-.8.5C4.8 7 3 5.2 2.7 3.4z" fill="#fff"/></symbol>
    <symbol id="icon-mail" viewBox="0 0 10 10"><circle cx="5" cy="5" r="5" fill="#0677BA"/><rect x="2.6" y="3.3" width="4.8" height="3.4" fill="none" stroke="#fff" stroke-width=".7"/><path d="M2.6 3.3 5 5.2l2.4-1.9" fill="none" stroke="#fff" stroke-width=".7"/></symbol>
    <symbol id="icon-web" viewBox="0 0 10 10"><circle cx="5" cy="5" r="5" fill="#0677BA"/><circle cx="5" cy="5" r="2.5" fill="none" stroke="#fff" stroke-width=".6"/><path d="M2.5 5h5M5 2.5c-1.2 1.4-1.2 3.6 0 5M5 2.5c1.2 1.4 1.2 3.6 0 5" fill="none" stroke="#fff" stroke-width=".5"/></symbol>
  </defs>
</svg>

<section class="card card--front" aria-label="Business card front">
  <div class="brand-mark"></div>
  <div class="brand-name">HARROW POINT<small>CONSULTING</small></div>
</section>

<section class="card card--back" aria-label="Business card back">
  <div class="watermark-ring"></div>
  <div class="brand">
    <div class="brand-mark"></div>
    <div class="brand-name">HARROW POINT<small>CONSULTING</small></div>
  </div>
  <div class="person">
    <div class="person__name">JOHN DOE</div>
    <div class="person__role">FOUNDER</div>
  </div>
  <ul class="contact-list">
    <li><svg class="contact-icon"><use href="#icon-phone"/></svg>(000) 0123 4567</li>
    <li><svg class="contact-icon"><use href="#icon-mail"/></svg>yourinfo@example.com</li>
    <li><svg class="contact-icon"><use href="#icon-web"/></svg>www.yourweb.com</li>
  </ul>
</section>

<section class="letterhead" aria-label="Letterhead">
  <div class="letterhead__band">
    <div class="brand-mark"></div>
    <div class="brand-name">HARROW POINT<small>CONSULTING</small></div>
  </div>
  <div class="letterhead__body">
    <div class="letterhead__to">To</div>
    <div class="recipient"><strong>Recipient Name</strong><br>Company Name<br>12 Street Road, City</div>
    <div class="letter-date">01 June 2024</div>
    <div>Dear Recipient,</div>
  </div>
  <div class="letterhead__text">
    <p>Thank you for meeting with our team last week. We have reviewed your network setup and prepared a short plan to strengthen access control and monitoring across all offices.</p>
    <p>The attached proposal outlines each step, the timeline and the expected cost. Please let us know a time that suits you to go through it together.</p>
    <div class="signoff">Kind regards,</div>
    <div class="signoff__name">John Doe</div>
  </div>
  <footer class="letterhead__footer">
    <span><svg class="contact-icon"><use href="#icon-phone"/></svg>(000) 0123 4567</span>
    <span><svg class="contact-icon"><use href="#icon-mail"/></svg>yourinfo@example.com</span>
    <span><svg class="contact-icon"><use href="#icon-web"/></svg>www.yourweb.com</span>
  </footer>
</section>
</body>
</html>
```